Pregnancy and Fertility Information Website

Hello Designers,
I need a website which provide tips and information about healthy and happy pregnancy. My website name is Lorvin medical.

The website should provide all the information needed throughout pregnancy and beyond ranging from pregnancy tracking tools and articles about common pregnancy concerns and what to expect during pregnancy,etc.
The details about first trimester, second trimester and third trimester should be highlighted in the website.

Top Navigation
Home, Fertility, Pregnancy basics, Articles, Tips and News

I'm looking for a simple and clean design which involves captivating images and colors but it shouldn't be crowded. The design must be professional and modern. An easy to navigate layout is a must.

Green, violet, blue and light yellow colors are my favorites but i'm open to other options.

Any questions. Kindly ask

Industry/Entity Type

Medical

```html
<!DOCTYPE html>
<html lang="en">
<head>
<meta charset="utf-8">
<title>Lorvin medical</title>
<link href="https://fonts.googleapis.com/css2?family=Cinzel:wght@400;600&family=Jost:wght@400;500;600&display=swap" rel="stylesheet">
<style>
:root{
  --blue:#0a68b5;
  --blue-dark:#075596;
  --green:#5bb947;
  --ink:#1d1d1d;
  --muted:#555;
  --line:#d6d6d6;
  --grey-band:#f1f1f1;
  --footer:#1c2124;
  --footer-bottom:#121618;
  --pink:#f6c7c7;
}
*{box-sizing:border-box;margin:0;padding:0}
html,body{width:1200px;height:2970px;overflow:hidden}
body{font-family:"Jost",Arial,sans-serif;color:var(--ink);background:#fff;position:relative}
.heading{font-family:"Cinzel",Georgia,serif;font-weight:600;font-size:38px;text-align:center;letter-spacing:1px;color:#111}
.heading .accent{color:var(--blue)}
.divider{display:flex;align-items:center;justify-content:center;gap:10px;margin-top:12px}
.divider span{display:block;width:210px;height:1px;background:var(--line)}
.divider i{display:block;width:14px;height:14px;border-radius:50%;border:2px solid var(--green);background:#9fd3f2}

/* header */
.site-header{position:absolute;top:0;left:0;width:1200px;height:96px;background:#fff;box-shadow:0 2px 6px rgba(0,0,0,.12);z-index:2}
.brand{position:absolute;left:112px;top:30px;display:flex;align-items:center;gap:10px;font-family:"Jost",sans-serif;font-weight:600;font-size:20px;color:var(--blue)}
.brand b{width:30px;height:30px;border-radius:50%;background:var(--green);display:block}
.nav{position:absolute;left:296px;top:0;display:flex;height:96px;align-items:center;list-style:none}
.nav li{font-family:"Cinzel",serif;font-size:15px;color:#333;padding:0 20px;height:96px;display:flex;align-items:center;position:relative}
.nav li+li::before{content:"";position:absolute;left:0;top:42px;height:14px;width:1px;background:#bbb}
.nav li.active{background:var(--blue);color:#fff;padding:0 16px}
.nav li.active+li::before{display:none}

/* hero */
.hero{position:absolute;top:96px;left:0;width:1200px;height:624px;background:linear-gradient(120deg,#c9d6df 0%,#e8e3de 40%,#b9b2ae 70%,#8a3b36 100%)}
.hero-caption{position:absolute;bottom:0;left:0;width:100%;height:100px;background:rgba(30,30,30,.6);color:#fff;font-family:"Cinzel",serif;font-size:26px;text-align:center;line-height:32px;padding-top:18px;letter-spacing:.5px}
.hero-badge{position:absolute;left:576px;top:698px;width:48px;height:48px;border-radius:50%;background:#fff;border:2px solid #ddd;z-index:1}

/* trimester */
.trimester{position:absolute;top:720px;left:0;width:1200px;height:592px}
.trimester .heading{margin-top:58px}
.silhouettes{position:absolute;left:150px;top:160px;width:900px;height:312px;background:linear-gradient(180deg,#fbe1e1,var(--pink));border-radius:6px;opacity:.85}
.tri-labels{position:absolute;top:488px;left:0;width:1200px}
.tri-group{position:absolute;text-align:center}
.tri-group .t{display:flex;align-items:center;gap:10px;font-family:"Cinzel",serif;font-size:11px;color:var(--green);justify-content:center}
.tri-group .t span{flex:1;height:1px;background:#bbb}
.tri-group .m{display:flex;justify-content:space-between;font-size:12px;color:#333;margin-top:26px;padding:0 14px}

/* fertility */
.fertility{position:absolute;top:1312px;left:0;width:1200px;height:364px;background:var(--blue);color:#fff;text-align:center}
.fertility::before,.fertility::after{content:"";position:absolute;left:582px;border-left:18px solid transparent;border-right:18px solid transparent}
.fertility::before{top:0;border-top:18px solid #fff}
.fertility::after{bottom:-18px;border-top:18px solid var(--blue)}
.fertility .heading{color:#fff;margin-top:50px}
.fertility .divider span{background:rgba(255,255,255,.4)}
.fertility h3{font-size:18px;font-weight:500;margin-top:28px}
.fertility p{font-size:13px;line-height:22px;width:1000px;margin:14px auto 0;color:#e8f1fa}
.btn-light{display:inline-block;margin-top:24px;background:#fff;color:#222;font-size:15px;padding:6px 24px}

/* articles */
.articles{position:absolute;top:1676px;left:0;width:1200px;height:586px}
.articles .heading{margin-top:68px}
.card{position:absolute;top:178px;width:304px;height:364px;border:1px solid #ddd;background:#fff}
.card .photo{height:182px;background:linear-gradient(160deg,#8fbf6a,#e58ab8)}
.card h4{font-size:14px;font-weight:500;margin:20px 16px 0}
.card .meta{font-size:11px;color:#777;margin:8px 16px 0}
.card p{font-size:12px;line-height:17px;margin:8px 16px 0;color:#333}
.btn{display:inline-block;background:var(--blue);color:#fff;font-size:15px;padding:6px 20px;margin:14px 16px 0}
.arrow{position:absolute;top:340px}

/* tips */
.tips{position:absolute;top:2262px;left:0;width:1200px;height:330px;background:var(--grey-band)}
.tips::before{content:"";position:absolute;left:584px;top:0;border-left:16px solid transparent;border-right:16px solid transparent;border-top:16px solid #fff}
.tips .heading{margin-top:58px}
.tip{position:absolute;top:170px;width:300px;display:flex;gap:14px}
.cal{width:92px;height:78px;flex:none;border:3px solid var(--blue);border-radius:8px;background:#fff;text-align:center;padding-top:12px;position:relative}
.cal::before{content:"";position:absolute;left:-3px;right:-3px;top:-3px;height:12px;background:var(--blue);border-radius:8px 8px 0 0}
.cal b{display:block;font-size:24px;font-weight:500;line-height:26px}
.cal small{font-size:15px}
.tip h5{font-size:14px;font-weight:600;line-height:18px}
.tip p{font-size:11px;line-height:16px;color:#333;margin-top:4px}
.tip a{font-size:11px;color:var(--green);text-decoration:underline;font-style:italic}

/* footer */
.site-footer{position:absolute;top:2592px;left:0;width:1200px;height:328px;background:var(--footer);color:#fff}
.field{position:absolute;left:120px;width:296px;border:1px solid #555;font-size:12px;color:#888;padding:8px 12px;height:38px}
.submit{position:absolute;left:120px;top:256px;background:var(--blue);color:#fff;font-size:15px;padding:6px 30px}
.vline{position:absolute;left:456px;top:60px;width:1px;height:240px;background:#444}
.contact{position:absolute;left:492px;display:flex;align-items:center;gap:20px}
.contact .ico{width:44px;height:44px;border-radius:50%;background:var(--blue);display:flex;align-items:center;justify-content:center}
.map{position:absolute;left:850px;top:66px;width:230px;height:230px;border-radius:50%;background:radial-gradient(circle,#e9e6dd,#b9cfe4);border:4px solid #fff}
.bottom-bar{position:absolute;top:2920px;left:0;width:1200px;height:50px;background:var(--footer-bottom);color:#ddd;font-size:13px;padding:14px 120px}
.socials{position:absolute;right:120px;top:10px;display:flex;gap:8px}
.socials span{width:30px;height:30px;border:1px solid #ddd;border-radius:50%}
</style>
</head>
<body>

<header class="site-header">
  <div class="brand"><b></b>Lorvin medical</div>
  <ul class="nav">
    <li class="active">Home</li>
    <li>Fertility</li>
    <li>Pregnancy Basics</li>
    <li>Articles</li>
    <li>Tips And News</li>
    <li>Contact Us</li>
  </ul>
</header>

<section class="hero" role="img" aria-label="Photograph of a smiling mother holding her newborn in a hospital bed, with the father beside her">
  <div class="hero-caption">The Pregnant Woman Guide To Protecting The<br>Pelvic Floor</div>
</section>
<div class="hero-badge"></div>

<section class="trimester">
  <h2 class="heading">Trimester <span class="accent">Chart</span></h2>
  <div class="divider"><span></span><i></i><span></span></div>
  <div class="silhouettes" role="img" aria-label="Illustration of nine pink silhouettes of a pregnant woman growing month by month"></div>
  <div class="tri-labels">
    <div class="tri-group" style="left:176px;width:240px"><div class="t"><span></span>1 Trimester<span></span></div><div class="m"><span>Month 1</span><span>Month 2</span><span>Month 3</span></div></div>
    <div class="tri-group" style="left:476px;width:240px"><div class="t"><span></span>2 Trimester<span></span></div><div class="m"><span>Month 4</span><span>Month 5</span><span>Month 6</span></div></div>
    <div class="tri-group" style="left:788px;width:240px"><div class="t"><span></span>3 Trimester<span></span></div><div class="m"><span>Month 7</span><span>Month 8</span><span>Month 9</span></div></div>
  </div>
</section>

<section class="fertility">
  <h2 class="heading">Fertility</h2>
  <div class="divider"><span></span><i></i><span></span></div>
  <h3>Duis autem vel eum iriure dolor in hendrerit in vulputate velit esse molestie consequat!</h3>
  <p>Lorem ipsum dolor sit amet, consectetuer adipiscing elit, sed diam nonummy nibh euismod tincidunt ut laoreet dolore magna aliquam erat volutpat. Ut wisi enim ad minim veniam, quis nostrud exerci tation ullamcorper suscipit lobortis nisl ut aliquip ex ea commodo consequat. Duis autem vel eum iriure dolor in hendrerit in vulputate velit esse molestie consequat, vel illum dolore eu feugiat nulla facilisis at vero eros et accumsan et iusto odio dignissim qui blandit praesent luptatum zzril delenit augue duis dolore te feugait nulla facilisi.</p>
  <span class="btn-light">Read More</span>
</section>

<section class="articles">
  <h2 class="heading">Recent <span class="accent">Articles</span></h2>
  <div class="divider"><span></span><i></i><span></span></div>
  <svg class="arrow" style="left:70px" width="24" height="40" viewBox="0 0 24 40"><path d="M20 2 4 20l16 18" fill="none" stroke="#6aa6d8" stroke-width="2"/></svg>
  <svg class="arrow" style="left:1106px" width="24" height="40" viewBox="0 0 24 40"><path d="M4 2l16 18L4 38" fill="none" stroke="#6aa6d8" stroke-width="2"/></svg>
  <article class="card" style="left:120px">
    <div class="photo" role="img" aria-label="Photograph of a pregnant woman sitting on grass"></div>
    <h4>Duis Aute Irure Dolor In Voluptate Velit</h4>
    <div class="meta">By Maria Keller 14 Feb 2017</div>
    <p>Ut enim ad minims veniam, quis nostrud nisit exercitation ullamco labor consequat.</p>
    <span class="btn">Read More</span>
  </article>
  <article class="card" style="left:448px">
    <div class="photo" role="img" aria-label="Photograph of a pregnant woman having an ultrasound scan" style="background:linear-gradient(160deg,#c9c2bd,#e78fb3)"></div>
    <h4>Duis Aute Irure Dolor In Voluptate Velit</h4>
    <div class="meta">By Maria Keller 13 Feb 2017</div>
    <p>Ut enim ad minims veniam, quis nostrud nisit exercitation ullamco labor consequat.</p>
    <span class="btn">Read More</span>
  </article>
  <article class="card" style="left:776px">
    <div class="photo" role="img" aria-label="Photograph of a mother holding her baby in a bright room" style="background:linear-gradient(160deg,#eef0f2,#d8cfc6)"></div>
    <h4>Duis Aute Irure Dolor In Voluptate Velit</h4>
    <div class="meta">By Maria Keller 11 Feb 2017</div>
    <p>Ut enim ad minims veniam, quis nostrud nisit exercitation ullamco labor consequat.</p>
    <span class="btn">Read More</span>
  </article>
</section>

<section class="tips">
  <h2 class="heading">Tips <span class="accent">&amp; News</span></h2>
  <div class="divider"><span></span><i></i><span></span></div>
  <div class="tip" style="left:120px"><div class="cal"><b>14<sup style="font-size:12px">th</sup></b><small>Feb</small></div><div><h5>Lorem Ipsum Dolor Sit Amet Consectetur Aliqua.</h5><p>Lorem Ipsum is simply dummy text of printing and typesetting industry.</p><a>Read More</a></div></div>
  <div class="tip" style="left:450px"><div class="cal"><b>13<sup style="font-size:12px">th</sup></b><small>Feb</small></div><div><h5>Lorem Ipsum Dolor Sit Amet Consectetur Aliqua.</h5><p>Lorem Ipsum is simply dummy text of printing and typesetting industry.</p><a>Read More</a></div></div>
  <div class="tip" style="left:780px"><div class="cal"><b>11<sup style="font-size:12px">th</sup></b><small>Feb</small></div><div><h5>Lorem Ipsum Dolor Sit Amet Consectetur Aliqua.</h5><p>Lorem Ipsum is simply dummy text of printing and typesetting industry.</p><a>Read More</a></div></div>
</section>

<footer class="site-footer">
  <div class="field" style="top:60px">Name</div>
  <div class="field" style="top:108px">Email</div>
  <div class="field" style="top:156px;height:90px">Message</div>
  <span class="submit">Submit</span>
  <div class="vline"></div>
  <div class="contact" style="top:64px">
    <div class="ico"><svg width="18" height="22" viewBox="0 0 18 22"><path d="M9 1a7 7 0 0 0-7 7c0 5 7 13 7 13s7-8 7-13a7 7 0 0 0-7-7z" fill="#fff"/><circle cx="9" cy="8" r="2.6" fill="#0a68b5"/></svg></div>
    <div><div style="font-size:15px">Lorvin medical</div><div style="font-size:12px;color:#aaa;line-height:17px;margin-top:4px">123, Ut wisi enim ad minim<br>veniam, quis nostrunl exercimori.</div></div>
  </div>
  <div class="contact" style="top:150px">
    <div class="ico"><svg width="20" height="20" viewBox="0 0 20 20"><path d="M4 1l4 4-2 3c1 2 4 5 6 6l3-2 4 4-3 3C9 19 1 11 1 4z" fill="#fff"/></svg></div>
    <div style="font-size:20px">123 456 7890</div>
  </div>
  <div class="contact" style="top:234px">
    <div class="ico"><svg width="20" height="14" viewBox="0 0 20 14"><rect width="20" height="14" rx="1" fill="#fff"/><path d="M1 1l9 7 9-7" fill="none" stroke="#0a68b5" stroke-width="1.5"/></svg></div>
    <div style="font-size:15px">info@lorvinmedical.com</div>
  </div>
  <div class="map" role="img" aria-label="Circular city map showing the clinic location"></div>
</footer>

<div class="bottom-bar">© 2017 Lorvin medical. All Right Reserved.
  <div class="socials"><span></span><span></span><span></span><span></span></div>
</div>

</body>
</html>
```